Plastic Jar Catalogue 7

We are a plastic factory manufacturing different size of plastic jars, which mostly use for spice and grinded coffee. I need the catalogue to be 3 pages:First page: an attractive cover shows the factory's name and logo with a space for products’ picture. Second page: is an items page which I prefer to be enough for 4 items with a space for item number and description under each item. Last page: to be for factory’s address and contact details.

```html
<!DOCTYPE html>
<html lang="en">
<head>
<meta charset="utf-8">
<title>Lumen Plastic Works – Jar Catalogue</title>
<link href="https://fonts.googleapis.com/css2?family=Playfair+Display:wght@400;700&family=Lora:ital,wght@1,400;1,700&display=swap" rel="stylesheet">
<style>
  :root{
    --backdrop:#fcf6ee;
    --mint:#8ccea9;
    --mint-light:#9dd6b7;
    --mint-deep:#72ae8d;
    --cream:#f7eda0;
    --sun:#fcc95a;
    --sun-light:#fbd47c;
    --sun-deep:#f0b23a;
    --coral:#f07272;
    --coral-deep:#e35f60;
    --lemon:#faf3b8;
    --lemon-deep:#ece39c;
    --ribbon:#ee5a5e;
    --white:#ffffff;
    --ink-soft:#b7ad6a;
  }
  *{box-sizing:border-box;margin:0;padding:0}
  html,body{width:1200px;height:706px;overflow:hidden;background:var(--backdrop)}
  body{position:relative;font-family:"Lora",Georgia,serif}

  .page{position:absolute;top:120px;width:364px;height:465px;box-shadow:0 1px 3px rgba(120,90,40,.18);overflow:hidden}
  .page--cover{left:41px;background:var(--mint)}
  .page--items{left:421px;background:var(--mint)}
  .page--contact{left:796px;background:var(--sun)}

  /* cover */
  .cover-title{position:absolute;left:40px;top:34px;font-family:"Playfair Display",Georgia,serif;font-weight:700;font-size:45px;line-height:42px;color:var(--cream);letter-spacing:.5px}
  .product-shot{position:absolute;border-radius:14px 14px 8px 8px}
  .cover-shot{top:182px;width:50px;height:145px;background:linear-gradient(90deg,#6fae8f,#a6dcc0 35%,#7cbb9b 70%,#6aa889)}
  .cover-shot--1{left:96px}.cover-shot--2{left:157px}.cover-shot--3{left:218px}
  .brand-mark{position:absolute;color:var(--white);font-family:"Lora",Georgia,serif;font-style:italic;font-weight:400;text-align:center;letter-spacing:2px;text-transform:uppercase}
  .brand-mark--cover{left:30px;top:372px;width:118px;font-size:11px;line-height:16px}

  /* items grid */
  .item{position:absolute;width:182px;height:232px;text-align:center}
  .item--tl{left:0;top:0;background:linear-gradient(180deg,var(--mint-light),var(--mint-deep) 62%,var(--mint) 63%,var(--mint))}
  .item--tr{left:182px;top:0;background:linear-gradient(180deg,var(--sun-light),var(--sun-deep) 62%,var(--sun) 63%,var(--sun-light))}
  .item--bl{left:0;top:233px;background:linear-gradient(180deg,var(--coral),var(--coral-deep) 62%,var(--coral) 63%,var(--coral-deep))}
  .item--br{left:182px;top:233px;background:linear-gradient(180deg,var(--lemon),var(--lemon-deep) 62%,var(--lemon) 63%,var(--lemon-deep))}
  .tag-string{position:absolute;left:41px;top:0;width:1px;height:24px;background:var(--cream)}
  .price-tag{position:absolute;left:17px;top:23px;width:48px;height:48px;border-radius:50%;border:3px dotted var(--cream);display:flex;align-items:center;justify-content:center;font-family:"Playfair Display",Georgia,serif;font-size:18px;color:var(--cream)}
  .price-tag--mint{background:var(--mint-deep)}
  .price-tag--orange{background:var(--sun-deep)}
  .price-tag--pink{background:#f48f8a}
  .price-tag--amber{background:#f6b94d}
  .item-shot{position:absolute;left:70px;top:26px;width:52px;height:144px}
  .item--tl .item-shot{background:linear-gradient(90deg,#79b595,#a9d9bf 40%,#86c1a2)}
  .item--tr .item-shot{background:linear-gradient(90deg,#e8c068,#fbe6a8 40%,#efc970);border-radius:18px 18px 6px 6px}
  .item--bl .item-shot{left:65px;width:64px;top:25px;background:linear-gradient(90deg,#ec9a98,#fbd4d2 40%,#e88384);border-radius:26px 26px 10px 10px}
  .item--br .item-shot{background:linear-gradient(90deg,#dcd597,#f7f3cf 40%,#dfd89b);border-radius:16px 16px 8px 8px}
  .item-number{position:absolute;left:0;right:0;top:173px;font-family:"Playfair Display",Georgia,serif;font-size:10px;color:var(--white)}
  .item-desc{position:absolute;left:10px;right:10px;top:195px;font-style:italic;font-size:7.1px;line-height:8.2px;color:var(--white)}
  .item-desc b{font-weight:700}
  .item--br .item-number,.item--br .item-desc{color:var(--ink-soft)}
  .new-ribbon{position:absolute;right:-34px;top:28px;width:150px;height:20px;background:var(--ribbon);transform:rotate(40deg);color:var(--cream);font-family:"Playfair Display",Georgia,serif;font-size:12px;line-height:20px;text-align:center}

  /* contact */
  .brand-mark--contact{left:62px;top:278px;width:240px;font-size:15px;line-height:20px;letter-spacing:3px}
  .contact{position:absolute;left:0;right:0;top:368px;text-align:center;font-style:italic;font-size:7.3px;line-height:8.2px;color:var(--white)}
</style>
</head>
<body>
  <section class="page page--cover">
    <h1 class="cover-title">LUMEN<br>PLASTIC<br>WORKS</h1>
    <div class="product-shot cover-shot cover-shot--1" role="img" aria-label="Clear plastic jar product photo"></div>
    <div class="product-shot cover-shot cover-shot--2" role="img" aria-label="Clear plastic jar product photo"></div>
    <div class="product-shot cover-shot cover-shot--3" role="img" aria-label="Clear plastic jar product photo"></div>
    <p class="brand-mark brand-mark--cover">Lumen Plastic<br>Works</p>
  </section>

  <section class="page page--items">
    <article class="item item--tl">
      <span class="tag-string"></span><span class="price-tag price-tag--mint">5$</span>
      <div class="product-shot item-shot" role="img" aria-label="Straight plastic jar product photo"></div>
      <p class="item-number">#123456</p>
      <p class="item-desc"><b>Lorem ipsum</b> dolor sit amet, consectetur adipiscing elit, sed do eiusmod tempor incididunt ut labore et dolore magna aliqua.</p>
    </article>
    <article class="item item--tr">
      <span class="tag-string"></span><span class="price-tag price-tag--orange">5$</span>
      <div class="product-shot item-shot" role="img" aria-label="Tall shaped plastic bottle product photo"></div>
      <p class="item-number">#123456</p>
      <p class="item-desc"><b>Lorem ipsum</b> dolor sit amet, consectetur adipiscing elit, sed do eiusmod tempor incididunt ut labore et dolore magna aliqua.</p>
    </article>
    <article class="item item--bl">
      <span class="tag-string"></span><span class="price-tag price-tag--pink">6$</span>
      <div class="product-shot item-shot" role="img" aria-label="Round-shouldered plastic jar product photo"></div>
      <p class="item-number">#123456</p>
      <p class="item-desc"><b>Lorem ipsum</b> dolor sit amet, consectetur adipiscing elit, sed do eiusmod tempor incididunt ut labore et dolore magna aliqua.</p>
    </article>
    <article class="item item--br">
      <span class="new-ribbon">NEW!</span>
      <span class="tag-string"></span><span class="price-tag price-tag--amber">6$</span>
      <div class="product-shot item-shot" role="img" aria-label="Ribbed plastic bottle product photo"></div>
      <p class="item-number">#123456</p>
      <p class="item-desc"><b>Lorem ipsum</b> dolor sit amet, consectetur adipiscing elit, sed do eiusmod tempor incididunt ut labore et dolore magna aliqua.</p>
    </article>
  </section>

  <section class="page page--contact">
    <p class="brand-mark brand-mark--contact">Lumen Plastic<br>Works</p>
    <address class="contact">
      214 Harbor Mill Road, Eastfield, Vermont<br>
      www.lumenplasticworks.com<br>
      hello@lumenplasticworks.com<br>
      0987 654 321
    </address>
  </section>
</body>
</html>
```